Präsentationsvorlagen
Zielgruppe
Wir sind ein Netzwerk aus unabhängigen Tierarztpraxen und-kliniken.
Aufgabenstellung
1. Allgemeine Anforderungen:
Wir benötigen ein Set an Masterfolien für unsere Präsentationen. Als Orientierung stellen wir Ihnen einige Beispielfolien im Anhang zur Verfügung, die eine grobe Vorstellung davon vermitteln, wie das Design aussehen soll. Zudem empfehlen wir, sich auf unserer Homepage umzusehen, um sicherzustellen, dass das Design mit unserem bestehenden Corporate Design harmoniert.
2. Farbkonzept:
Bitte verwenden Sie unsere definierten Unternehmensfarben:
Gelb: #f7cd4e
Blau: #143357
Gold: #9d8030
Weiß: #ffffff
3. Schriftarten:
Unsere Unternehmensschriftarten sind:
Raleway
Century Gothic
Bitte stellen Sie sicher, dass diese Fonts durchgehend verwendet werden.
4. Farbvarianten:
Wir wünschen uns drei unterschiedliche Farbvarianten der Masterfolien:
Blaue Version: mit Blau als dominierende Farbe
Gelbe Version: mit Gelb als dominierende Farbe
Neutrale Version: weiß dominierend mit - eine ausgewogene Mischung mit gedeckteren Farben
5. Design-Elemente:
Das Design sollte modern, professionell und klar strukturiert sein.
Die Masterfolien sollen verschiedene Layouts enthalten (Titelfolie, Inhaltsfolie, Bild-Text-Kombinationen, etc.).
Bitte achten Sie darauf, dass genügend weißer Raum für eine aufgeräumte und übersichtliche Gestaltung bleibt.
Elemente wie Linien, Icons oder dezente Muster können genutzt werden, sollten jedoch nicht zu dominant wirken.
6. Format:
Die Masterfolien sollten für Microsoft PowerPoint optimiert sein und in 16:9 Format erstellt werden.

```html
<!DOCTYPE html>
<html lang="de">
<head>
<meta charset="utf-8">
<title>KLAROVEN – Masterfolien</title>
<link href="https://fonts.googleapis.com/css2?family=Raleway:ital,wght@0,400;0,500;0,600;0,700;0,800;1,400;1,600&display=swap" rel="stylesheet">
<style>
:root{
  --blue:#143357;
  --blue-deep:#0f2846;
  --yellow:#f7cd4e;
  --gold:#9d8030;
  --white:#ffffff;
  --page:#f4f4f4;
  --stage:#182a46;
  --line:rgba(255,255,255,.25);
}
*{box-sizing:border-box;margin:0;padding:0}
html,body{width:1200px;height:3517px;overflow:hidden}
body{background:var(--page);font-family:'Raleway',sans-serif;color:var(--white);position:relative}
.stage{position:absolute;left:0;top:0;width:1200px;height:800px;background:var(--stage)}
.slide{position:absolute;width:526px;height:295px;background:var(--blue);overflow:hidden}
.c1{left:75px}.c2{left:631px}
.r1{top:883px}.r2{top:1203px}.r3{top:1523px}.r4{top:1843px}
.r5{top:2162px}.r6{top:2482px}.r7{top:2802px}.r8{top:3123px}
.abs{position:absolute}
.title-bar{position:absolute;left:40px;top:30px;width:22px;height:3px;background:var(--yellow)}
.title{position:absolute;left:40px;top:36px;font-size:20px;font-weight:700;letter-spacing:.2px}
.mark{position:absolute;top:16px;right:22px;width:40px;text-align:center}
.mark i{display:block;width:16px;height:16px;margin:0 auto 2px;background:var(--gold);border-radius:3px}
.mark b{font-size:5px;font-weight:700;color:var(--yellow);letter-spacing:.2px}
.foot{position:absolute;left:20px;bottom:13px;font-size:5.5px;opacity:.85}
.pg{position:absolute;right:0;bottom:0;width:62px;height:23px;background:var(--yellow);border-top-left-radius:11px;color:var(--blue);font-size:19px;font-weight:700;text-align:center;line-height:24px}
.txt{font-size:6.6px;line-height:1.55}
.lead{font-size:6.8px;line-height:1.55;font-weight:700}
.y{color:var(--yellow)}
.photo{position:absolute;border-radius:10px}
.ph-vet{background:linear-gradient(135deg,#cfd3da,#8a96a8 60%,#3e5170)}
.ph-green{background:linear-gradient(120deg,#e5e7ea,#9aa3ad 45%,#2f8a3c 80%,#1f6a2b)}
.ph-portrait{background:linear-gradient(160deg,#eef0f3,#b8bec8 55%,#2c3e58)}
.ph-grey{background:linear-gradient(180deg,#f0f1f3,#c9ced6)}
.ph-clinic{background:linear-gradient(135deg,#ffffff,#e3e6ea 55%,#b4bcc6)}
.ph-dog{background:linear-gradient(160deg,#e8d3a6,#c79d5c 60%,#6c5030)}
.ph-hands{background:linear-gradient(140deg,#7f8ea4,#c9a88c 50%,#34496a)}
.tile{position:absolute;border-radius:8px}
.logo{position:absolute;display:flex;align-items:center;gap:7px}
.logo i{width:22px;height:22px;background:var(--gold);border-radius:4px}
.logo b{font-size:21px;font-weight:600;color:var(--yellow);letter-spacing:.3px}
.hero{position:absolute;font-size:25px;font-weight:700;line-height:1.18}
.btn{position:absolute;height:22px;background:var(--yellow);border-radius:11px;color:var(--blue);font-size:9px;font-weight:700;display:flex;align-items:center;gap:9px;padding-left:16px}
.btn svg{width:10px;height:10px}
.meta{position:absolute;bottom:12px;font-size:5px;opacity:.85}
/* agenda */
.ag{position:absolute;width:150px;font-size:6px;line-height:1.5}
.ag .n{position:absolute;left:-26px;top:0;color:var(--yellow);font-weight:700;font-size:7px}
.ag b{color:var(--yellow);font-weight:700}
.ag li{list-style:none}
.ag li::before{content:"• "}
.row{position:absolute;left:268px;width:200px;font-size:6.4px;line-height:1.5;padding:0 0 7px 28px;border-bottom:1px solid var(--line)}
.row b{position:absolute;left:0;top:0;color:var(--yellow);font-size:6.4px}
/* panels */
.panel{position:absolute;top:118px;width:106px;height:122px;background:var(--yellow);border-radius:8px;color:var(--blue);padding:30px 10px 0 16px;font-size:6px;line-height:1.55}
.panel .ic{position:absolute;left:-4px;top:-6px;width:30px;height:30px;border:2px solid var(--white);background:var(--blue);border-radius:7px;display:flex;align-items:center;justify-content:center}
.panel .ic svg{width:17px;height:17px;color:var(--white)}
.panel .h{position:absolute;left:34px;top:5px;font-weight:700;font-size:6px;line-height:1.35}
.ic svg{display:block}
/* quote */
.quote{position:absolute;left:298px;top:72px;width:182px;height:174px;background:var(--yellow);border-radius:10px;color:var(--blue);padding:34px 16px 0;font-size:6.5px;line-height:1.6;font-style:italic}
.quote .qm{position:absolute;left:0;right:0;top:10px;text-align:center;font-size:28px;font-weight:800;font-style:normal;line-height:1}
.quote .by{text-align:right;margin-top:10px}
/* quartals */
.q{position:absolute;width:75px;height:75px;color:var(--blue);font-size:9px;font-weight:700;display:flex;align-items:center;justify-content:center;text-align:center;line-height:1.2}
.q.w{background:var(--white)}.q.yl{background:var(--yellow)}
.plist{position:absolute;font-size:5.8px;line-height:1.6;width:110px}
.plist b{display:block;font-weight:700;margin-bottom:2px}
.plist li{list-style:none}
.plist li::before{content:"• "}
.conn{position:absolute;height:1px;background:var(--white)}
/* service cards */
.svc{position:absolute;width:208px;height:78px;background:var(--white);border-radius:9px;color:var(--blue);padding:14px 12px 0 72px;font-size:6.3px;line-height:1.55}
.svc b{display:block;font-weight:700}
.svc .ic{position:absolute;left:8px;top:9px;width:58px;height:60px;background:var(--yellow);border-radius:8px;display:flex;align-items:center;justify-content:center}
.svc .ic svg{width:30px;height:30px;color:var(--blue)}
.svc .ic.o{background:var(--white);border:2px solid var(--yellow)}
.pill{position:absolute;left:279px;width:197px;height:30px;background:var(--white);border-radius:8px;color:var(--blue);font-size:6px;font-weight:700;line-height:1.45;padding:6px 0 0 13px}
.pill .ic{position:absolute;right:6px;top:4px;width:22px;height:22px;border:1.5px solid var(--yellow);border-radius:50%;display:flex;align-items:center;justify-content:center}
.pill .ic svg{width:13px;height:13px;color:var(--blue)}
/* team */
.band{position:absolute;left:0;right:0;bottom:0;height:67px;background:var(--yellow)}
.card{position:absolute;top:89px;width:108px;height:169px;background:var(--white);border-radius:9px;color:var(--blue);overflow:hidden;text-align:center}
.card .face{height:72px;background:linear-gradient(180deg,#eff1f4,#c3c9d2)}
.card b{display:block;font-size:6.6px;margin-top:4px}
.card small{display:block;font-size:5.5px;opacity:.8}
.card ul{text-align:left;margin:9px 0 0 18px;font-size:6px;line-height:1.6;list-style:none}
.card li::before{content:"• "}
.mname{position:absolute;left:102px;top:224px;width:125px;text-align:center}
.mname b{display:block;font-size:9.5px;color:var(--yellow);font-weight:700}
.mname small{display:block;font-size:7px;font-weight:600}
/* three column */
.col{position:absolute;width:140px;font-size:6.3px;line-height:1.55}
.col .n{font-size:16px;color:var(--yellow);font-weight:500;margin-bottom:4px}
.col b{display:block;margin-bottom:5px}
.vline{position:absolute;width:1px;background:var(--line)}
</style>
</head>
<body>
<svg width="0" height="0" style="position:absolute" aria-hidden="true">
  <symbol id="i-badge" viewBox="0 0 24 24"><circle cx="12" cy="12" r="9" fill="none" stroke="currentColor" stroke-width="1.8"/><path d="M7.5 12.3l3 3 6-6" fill="none" stroke="currentColor" stroke-width="1.8" stroke-linecap="round" stroke-linejoin="round"/></symbol>
  <symbol id="i-clock" viewBox="0 0 24 24"><circle cx="12" cy="12" r="9" fill="none" stroke="currentColor" stroke-width="1.8"/><path d="M12 7v5l3.5 2" fill="none" stroke="currentColor" stroke-width="1.8" stroke-linecap="round"/></symbol>
  <symbol id="i-hand" viewBox="0 0 24 24"><circle cx="14" cy="6" r="3.2" fill="none" stroke="currentColor" stroke-width="1.8"/><path d="M3 15h4l4 2h5a2 2 0 0 0 0-4h-4M7 19l3 2h6l5-5" fill="none" stroke="currentColor" stroke-width="1.8" stroke-linecap="round" stroke-linejoin="round"/></symbol>
  <symbol id="i-move" viewBox="0 0 24 24"><path d="M12 3v18M3 12h18M12 3l-3 3M12 3l3 3M12 21l-3-3M12 21l3-3M3 12l3-3M3 12l3 3M21 12l-3-3M21 12l-3 3" fill="none" stroke="currentColor" stroke-width="1.8" stroke-linecap="round"/></symbol>
  <symbol id="i-play" viewBox="0 0 10 10"><path d="M1 0l9 5-9 5z" fill="currentColor"/></symbol>
</svg>

<div class="stage"></div>

<!-- Title slide -->
<section class="slide c1 r1">
  <div class="logo" style="left:38px;top:40px"><i></i><b>KLAROVEN</b></div>
  <h1 class="hero" style="left:35px;top:118px">Your Presentation<br>Title <span class="y">Goes Here</span></h1>
  <div class="btn" style="left:35px;top:188px;width:183px"><svg><use href="#i-play"/></svg>Lorem ipsum dolor sit amet</div>
  <div class="meta" style="left:35px">07 Februar 2025 | Created by Max Mustermann</div>
  <div class="tile ph-grey" style="left:279px;top:-6px;width:110px;height:80px" role="img" aria-label="Foto: Praxisteam am Empfang"></div>
  <div class="tile ph-green" style="left:279px;top:84px;width:110px;height:165px" role="img" aria-label="Foto: Tierärztin mit Hund"></div>
  <div class="tile ph-grey" style="left:279px;top:258px;width:110px;height:50px" role="img" aria-label="Foto: Behandlungsraum"></div>
  <div class="tile ph-grey" style="left:398px;top:-6px;width:134px;height:54px" role="img" aria-label="Foto: Praxisflur"></div>
  <div class="tile ph-hands" style="left:398px;top:58px;width:134px;height:135px" role="img" aria-label="Foto: Team legt Hände übereinander"></div>
  <div class="tile ph-dog" style="left:398px;top:202px;width:134px;height:100px" role="img" aria-label="Foto: Golden Retriever"></div>
  <div class="meta" style="left:385px;font-size:5px">info@klarovenberg.de | www.klarovenberg.de</div>
</section>

<!-- Agenda 01-06 -->
<section class="slide c2 r1">
  <div class="title-bar"></div><h2 class="title">Today’s Agenda</h2>
  <div class="mark"><i></i><b>KLAROVEN</b></div>
  <div class="ag" style="left:127px;top:117px"><span class="n">01</span><b>Lorem ipsum dolor sit amet</b><ul><li>Lorem ipsum dolor sit amet</li><li>Lorem ipsum dolor sit amet</li></ul></div>
  <div class="ag" style="left:298px;top:117px"><span class="n">02</span><b>Lorem ipsum dolor sit amet</b><ul><li>Lorem ipsum dolor sit amet</li><li>Lorem ipsum dolor sit amet</li></ul></div>
  <div class="ag" style="left:171px;top:166px"><span class="n">03</span><b>Lorem ipsum dolor sit amet</b><ul><li>Lorem ipsum dolor sit amet</li><li>Lorem ipsum dolor sit amet</li></ul></div>
  <div class="ag" style="left:343px;top:166px"><span class="n">04</span><b>Lorem ipsum dolor sit amet</b><ul><li>Lorem ipsum dolor sit amet</li><li>Lorem ipsum dolor sit amet</li></ul></div>
  <div class="ag" style="left:199px;top:213px"><span class="n">05</span><b>Lorem ipsum dolor sit amet</b><ul><li>Lorem ipsum dolor sit amet</li><li>Lorem ipsum dolor sit amet</li></ul></div>
  <div class="ag" style="left:371px;top:213px"><span class="n">06</span><b>Lorem ipsum dolor sit amet</b><ul><li>Lorem ipsum dolor sit amet</li><li>Lorem ipsum dolor sit amet</li></ul></div>
</section>

<!-- Agenda with photo -->
<section class="slide c1 r2">
  <div class="title-bar"></div><h2 class="title">Today’s Agenda</h2>
  <div class="mark"><i></i><b>KLAROVEN</b></div>
  <div class="photo ph-portrait" style="left:42px;top:85px;width:164px;height:173px;border-radius:14px" role="img" aria-label="Foto: Tierärztin im Gespräch am Laptop"></div>
  <div class="row" style="top:92px"><b>01</b>Lorem ipsum dolor sit amet, consectetuer adipiscing elit, sed diam nonummy.</div>
  <div class="row" style="top:137px"><b>02</b>Lorem ipsum dolor sit amet, consectetuer adipiscing elit, sed diam nonummy.</div>
  <div class="row" style="top:182px"><b>03</b>Lorem ipsum dolor sit amet, consectetuer adipiscing elit, sed diam nonummy.</div>
  <div class="row" style="top:227px;border-bottom:0"><b>04</b>Lorem ipsum dolor sit amet, consectetuer adipiscing elit, sed diam nonummy.</div>
</section>

<!-- One long column -->
<section class="slide c2 r2">
  <div class="title-bar"></div><h2 class="title" style="font-size:18px">One Long Column</h2>
  <div class="mark"><i></i><b>KLAROVEN</b></div>
  <p class="lead abs" style="left:40px;top:92px;width:220px">Lorem ipsum dolor sit amet, consectetuer adipiscing elit, sed diam nonummy nibh euismod tincidunt.</p>
  <p class="txt abs" style="left:40px;top:128px;width:446px">Lorem ipsum dolor sit amet, consectetuer adipiscing elit, sed diam nonummy nibh euismod tincidunt ut laoreet dolore magna aliquam erat volutpat. Ut wisi enim ad minim veniam, quis nostrud exerci tation ullamcorper suscipit lobortis nisl ut aliquip ex ea commodo consequat. Duis autem vel eum iriure dolor in hendrerit in vulputate velit esse molestie consequat, vel illum dolore eu feugiat nulla.</p>
  <p class="txt abs" style="left:40px;top:185px;width:446px">Lorem ipsum dolor sit amet, consectetuer adipiscing elit, sed diam nonummy nibh euismod tincidunt ut laoreet dolore magna aliquam erat volutpat. Ut wisi enim ad minim veniam, quis nostrud exerci tation ullamcorper suscipit lobortis nisl ut aliquip ex ea commodo consequat. Duis autem vel eum iriure dolor in hendrerit in vulputate velit esse molestie consequat, vel illum dolore eu feugiat nulla.</p>
  <div class="foot">Your presentation Title Goes Here | www.klarovenberg.de</div>
  <div class="pg">02</div>
</section>

<!-- Four panel point -->
<section class="slide c1 r3">
  <div class="title-bar"></div><h2 class="title">Four Panel Point</h2>
  <div class="mark"><i></i><b>KLAROVEN</b></div>
  <p class="txt abs" style="left:40px;top:78px;width:450px">Lorem ipsum dolor sit amet, consectetuer adipiscing elit, sed diam nonummy nibh euismod tincidunt ut laoreet dolore magna aliquam erat volutpat. Ut wisi enim ad minim veniam.</p>
  <div class="panel" style="left:34px"><div class="ic"><svg><use href="#i-badge"/></svg></div><div class="h">Lorem ipsum<br>dolor sit amet.</div>Lorem ipsum dolor sit amet, consectetuer adipiscing elit, sed diam nonummy nibh euismod tincidunt ut laoreet dolore magna aliquam erat volutpat.</div>
  <div class="panel" style="left:152px"><div class="ic"><svg><use href="#i-hand"/></svg></div><div class="h">Lorem ipsum<br>dolor sit amet.</div>Lorem ipsum dolor sit amet, consectetuer adipiscing elit, sed diam nonummy nibh euismod tincidunt ut laoreet dolore magna aliquam erat volutpat.</div>
  <div class="panel" style="left:270px"><div class="ic"><svg><use href="#i-clock"/></svg></div><div class="h">Lorem ipsum<br>dolor sit amet.</div>Lorem ipsum dolor sit amet, consectetuer adipiscing elit, sed diam nonummy nibh euismod tincidunt ut laoreet dolore magna aliquam erat volutpat.</div>
  <div class="panel" style="left:387px"><div class="ic"><svg><use href="#i-move"/></svg></div><div class="h">Lorem ipsum<br>dolor sit amet.</div>Lorem ipsum dolor sit amet, consectetuer adipiscing elit, sed diam nonummy nibh euismod tincidunt ut laoreet dolore magna aliquam erat volutpat.</div>
  <div class="foot">Your presentation Title Goes Here | www.klarovenberg.de</div>
  <div class="pg">03</div>
</section>

<!-- Image with text -->
<section class="slide c2 r3">
  <div class="title-bar"></div><h2 class="title">Image With Text</h2>
  <div class="mark"><i></i><b>KLAROVEN</b></div>
  <p class="lead abs" style="left:40px;top:78px;width:210px">Lorem ipsum dolor sit amet, consectetuer adipiscing elit, sed diam nonummy nibh euismod tincidunt.</p>
  <p class="txt abs" style="left:40px;top:112px;width:222px">Lorem ipsum dolor sit amet, consectetuer adipiscing elit, sed diam nonummy nibh euismod tincidunt ut laoreet dolore magna aliquam erat volutpat. Ut wisi enim ad minim veniam, quis nostrud exerci tation ullamcorper suscipit lobortis nisl ut aliquip ex ea commodo consequat.</p>
  <div class="abs" style="left:40px;top:196px;width:3px;height:28px;background:var(--yellow)"></div>
  <p class="txt abs" style="left:52px;top:194px;width:206px;font-style:italic;color:var(--yellow)">Lorem ipsum dolor sit amet, consectetuer adipiscing elit, sed diam nonummy nibh euismod tincidunt ut laoreet dolore magna aliquam erat volutpat.</p>
  <div class="photo ph-green" style="left:274px;top:74px;width:212px;height:177px" role="img" aria-label="Foto: Tierarzt untersucht ein Pferd"></div>
  <div class="foot">Your presentation Title Goes Here | www.klarovenberg.de</div>
  <div class="pg">04</div>
</section>

<!-- Single paragraph -->
<section class="slide c1 r4">
  <div class="title-bar"></div><h2 class="title">Single Paragraph</h2>
  <div class="mark"><i></i><b>KLAROVEN</b></div>
  <p class="lead abs" style="left:40px;top:96px;width:215px">Lorem ipsum dolor sit amet, consectetuer adipiscing elit, sed diam nonummy nibh euismod tincidunt.</p>
  <p class="txt abs" style="left:40px;top:130px;width:222px">Lorem ipsum dolor sit amet, consectetuer adipiscing elit, sed diam nonummy nibh euismod tincidunt ut laoreet dolore magna aliquam erat volutpat. Ut wisi enim ad minim veniam, quis nostrud exerci tation ullamcorper suscipit lobortis nisl ut aliquip ex ea commodo consequat. Duis autem vel eum iriure dolor in hendrerit in vulputate velit esse molestie consequat, vel illum dolore eu feugiat nulla.</p>
  <div class="quote"><div class="qm">“</div>Lorem ipsum dolor sit amet, consectetuer adipiscing elit, sed diam nonummy nibh euismod tincidunt ut laoreet dolore magna aliquam erat volutpat. Ut wisi enim ad minim veniam, quis nostrud exerci tation ullamcorper suscipit lobortis nisl ut aliquip ex ea commodo consequat, dolore eu feugiat nulla<div class="by">Lorem ipsum dolor sit amet</div></div>
  <div class="foot">Your presentation Title Goes Here | www.klarovenberg.de</div>
  <div class="pg">05</div>
</section>

<!-- Project overview -->
<section class="slide c2 r4">
  <div class="title-bar"></div><h2 class="title">Project Overview</h2>
  <div class="mark"><i></i><b>KLAROVEN</b></div>
  <div class="plist" style="left:42px;top:88px"><b>Quartal 1 Projects</b><ul><li>Project 1 Name goes here</li><li>Project 2 Name goes here</li><li>Project 3 Name goes here</li><li>Project 4 Name goes here</li></ul></div>
  <div class="plist" style="left:42px;top:178px"><b>Quartal 3 Projects</b><ul><li>Project 1 Name goes here</li><li>Project 2 Name goes here</li><li>Project 3 Name goes here</li><li>Project 4 Name goes here</li></ul></div>
  <div class="plist" style="left:392px;top:88px"><b>Quartal 2 Projects</b><ul><li>Project 1 Name goes here</li><li>Project 2 Name goes here</li><li>Project 3 Name goes here</li><li>Project 4 Name goes here</li></ul></div>
  <div class="plist" style="left:392px;top:178px"><b>Quartal 4 Projects</b><ul><li>Project 1 Name goes here</li><li>Project 2 Name goes here</li><li>Project 3 Name goes here</li><li>Project 4 Name goes here</li></ul></div>
  <div class="conn" style="left:118px;top:93px;width:78px"></div>
  <div class="conn" style="left:118px;top:183px;width:78px"></div>
  <div class="conn" style="left:334px;top:93px;width:52px"></div>
  <div class="conn" style="left:334px;top:183px;width:52px"></div>
  <div class="q w" style="left:186px;top:76px;border-top-left-radius:22px">Quartal<br>One</div>
  <div class="q yl" style="left:269px;top:76px;border-top-right-radius:22px">Quartal<br>Two</div>
  <div class="q yl" style="left:186px;top:160px;border-bottom-left-radius:22px">Quartal<br>Three</div>
  <div class="q w" style="left:269px;top:160px;border-bottom-right-radius:22px">Quartal<br>Four</div>
  <div class="foot">Your presentation Title Goes Here | www.klarovenberg.de</div>
  <div class="pg">06</div>
</section>

<!-- Our service cards -->
<section class="slide c1 r5">
  <div class="title-bar"></div><h2 class="title">Our Service</h2>
  <div class="mark"><i></i><b>KLAROVEN</b></div>
  <div class="svc" style="left:49px;top:76px"><div class="ic"><svg><use href="#i-badge"/></svg></div><b>Lorem ipsum dolor sit amet.</b>Lorem ipsum dolor sit amet, consectetuer adipiscing elit, sed diam nonummy nibh euismod.</div>
  <div class="svc" style="left:270px;top:76px"><div class="ic o"><svg><use href="#i-clock"/></svg></div><b>Lorem ipsum dolor sit amet.</b>Lorem ipsum dolor sit amet, consectetuer adipiscing elit, sed diam nonummy nibh euismod.</div>
  <div class="svc" style="left:49px;top:169px"><div class="ic"><svg><use href="#i-hand"/></svg></div><b>Lorem ipsum dolor sit amet.</b>Lorem ipsum dolor sit amet, consectetuer adipiscing elit, sed diam nonummy nibh euismod.</div>
  <div class="svc" style="left:270px;top:169px"><div class="ic"><svg><use href="#i-move"/></svg></div><b>Lorem ipsum dolor sit amet.</b>Lorem ipsum dolor sit amet, consectetuer adipiscing elit, sed diam nonummy nibh euismod.</div>
  <div class="foot">Your presentation Title Goes Here | www.klarovenberg.de</div>
  <div class="pg">11</div>
</section>

<!-- Our team single -->
<section class="slide c2 r5">
  <div class="title-bar"></div><h2 class="title" style="line-height:1.2">Our<br>Team</h2>
  <div class="mark"><i></i><b>KLAROVEN</b></div>
  <div class="photo ph-portrait" style="left:102px;top:72px;width:125px;height:182px;border-radius:8px" role="img" aria-label="Porträtfoto: Geschäftsführer der Praxis"></div>
  <div class="mname"><b>Dr. Tomas Reinhold</b><small>Geschäftsführer</small></div>
  <p class="txt abs" style="left:254px;top:78px;width:236px;font-style:italic;font-weight:600;color:var(--yellow)">Lorem ipsum dolor sit amet, consectetuer adipiscing elit, sed diam nonummy nibh euismod tincidunt.</p>
  <p class="txt abs" style="left:254px;top:104px;width:236px">Lorem ipsum dolor sit amet, consectetuer adipiscing elit, sed diam nonummy nibh euismod tincidunt ut laoreet dolore magna aliquam erat volutpat.</p>
  <p class="txt abs" style="left:254px;top:140px;width:236px;padding-left:18px"><b class="y abs" style="left:0">01</b>Lorem ipsum dolor sit amet, consectetuer adipiscing elit, sed diam nonummy nibh euismod.</p>
  <p class="txt abs" style="left:254px;top:170px;width:236px;padding-left:18px"><b class="y abs" style="left:0">02</b>Lorem ipsum dolor sit amet, consectetuer adipiscing elit, sed diam nonummy nibh euismod.</p>
  <p class="txt abs" style="left:254px;top:200px;width:236px;padding-left:18px"><b class="y abs" style="left:0">03</b>Lorem ipsum dolor sit amet, consectetuer adipiscing elit, sed diam nonummy nibh euismod.</p>
  <div class="foot">Your presentation Title Goes Here | www.klarovenberg.de</div>
  <div class="pg">07</div>
</section>

<!-- Our service with image -->
<section class="slide c1 r6">
  <div class="title-bar"></div><h2 class="title">Our Service</h2>
  <div class="mark"><i></i><b>KLAROVEN</b></div>
  <div class="photo ph-clinic" style="left:42px;top:71px;width:201px;height:180px" role="img" aria-label="Foto: Computertomograph in der Klinik"></div>
  <div class="pill" style="top:75px">Lorem ipsum dolor sit amet,<br>consectetuer adipiscing elit, sed diam.<div class="ic"><svg><use href="#i-badge"/></svg></div></div>
  <div class="pill" style="top:120px">Lorem ipsum dolor sit amet,<br>consectetuer adipiscing elit, sed diam.<div class="ic"><svg><use href="#i-clock"/></svg></div></div>
  <div class="pill" style="top:165px">Lorem ipsum dolor sit amet,<br>consectetuer adipiscing elit, sed diam.<div class="ic"><svg><use href="#i-hand"/></svg></div></div>
  <div class="pill" style="top:210px">Lorem ipsum dolor sit amet,<br>consectetuer adipiscing elit, sed diam.<div class="ic"><svg><use href="#i-move"/></svg></div></div>
  <div class="foot">Your presentation Title Goes Here | www.klarovenberg.de</div>
  <div class="pg">12</div>
</section>

<!-- Our team cards -->
<section class="slide c2 r6">
  <div class="title-bar"></div><h2 class="title">Our Team</h2>
  <div class="mark"><i></i><b>KLAROVEN</b></div>
  <div class="band"></div>
  <div class="card" style="left:40px"><div class="face" role="img" aria-label="Porträtfoto Teammitglied"></div><b>Dr. Tomas Reinhold</b><small>Geschäftsführer</small><ul><li>Project 1 Name</li><li>Project 1 Name</li><li>Project 1 Name</li><li>Project 1 Name</li></ul></div>
  <div class="card" style="left:159px"><div class="face" role="img" aria-label="Porträtfoto Teammitglied"></div><b>Gerda Albrecht</b><small>Geschäftsführerin</small><ul><li>Project 1 Name</li><li>Project 1 Name</li><li>Project 1 Name</li><li>Project 1 Name</li></ul></div>
  <div class="card" style="left:278px"><div class="face" role="img" aria-label="Porträtfoto Teammitglied"></div><b>Jonas Falk</b><small>Geschäftsführer</small><ul><li>Project 1 Name</li><li>Project 1 Name</li><li>Project 1 Name</li><li>Project 1 Name</li></ul></div>
  <div class="card" style="left:396px"><div class="face" role="img" aria-label="Porträtfoto Teammitglied"></div><b>Marlene Hartwig</b><small>Geschäftsführerin</small><ul><li>Project 1 Name</li><li>Project 1 Name</li><li>Project 1 Name</li><li>Project 1 Name</li></ul></div>
  <div class="foot" style="color:var(--blue)">Your presentation Title Goes Here | www.klarovenberg.de</div>
  <div class="pg" style="background:var(--blue);color:var(--white)">08</div>
</section>

<!-- Three column -->
<section class="slide c1 r7">
  <div class="title-bar"></div><h2 class="title">Three Column</h2>
  <div class="mark"><i></i><b>KLAROVEN</b></div>
  <div class="col" style="left:40px;top:96px;width:125px"><div class="n">01</div><b>Lorem ipsum dolor sit amet, consectetuer adipiscing.</b>Lorem ipsum dolor sit amet, consectetuer adipiscing elit, sed diam nonummy nibh euismod tincidunt ut laoreet dolore magna aliquam erat volutpat. Ut wisi enim ad minim veniam, quis nostrud exerci tation ullamcorper suscipit lobortis nisl ut aliquip ex ea.</div>
  <div class="vline" style="left:176px;top:96px;height:150px"></div>
  <div class="col" style="left:200px;top:96px;width:125px"><div class="n">02</div><b>Lorem ipsum dolor sit amet, consectetuer adipiscing.</b>Lorem ipsum dolor sit amet, consectetuer adipiscing elit, sed diam nonummy nibh euismod tincidunt ut laoreet dolore magna aliquam erat volutpat. Ut wisi enim ad minim veniam, quis nostrud exerci tation ullamcorper suscipit lobortis nisl ut aliquip ex ea.</div>
  <div class="vline" style="left:336px;top:96px;height:150px"></div>
  <div class="col" style="left:360px;top:96px;width:125px"><div class="n">03</div><b>Lorem ipsum dolor sit amet, consectetuer adipiscing.</b>Lorem ipsum dolor sit amet, consectetuer adipiscing elit, sed diam nonummy nibh euismod tincidunt ut laoreet dolore magna aliquam erat volutpat. Ut wisi enim ad minim veniam, quis nostrud exerci tation ullamcorper suscipit lobortis nisl ut aliquip ex ea.</div>
  <div class="foot">Your presentation Title Goes Here | www.klarovenberg.de</div>
  <div class="pg">10</div>
</section>

<!-- Three column with intro -->
<section class="slide c2 r7">
  <div class="title-bar"></div><h2 class="title">Three Column</h2>
  <div class="mark"><i></i><b>KLAROVEN</b></div>
  <p class="txt abs" style="left:40px;top:70px;width:440px">Lorem ipsum dolor sit amet, consectetuer adipiscing elit, sed diam nonummy nibh euismod tincidunt ut laoreet dolore magna aliquam erat volutpat. Ut wisi enim ad minim veniam, quis nostrud exerci tation ullamcorper suscipit lobortis nisl ut aliquip ex ea commodo consequat.</p>
  <div class="col" style="left:40px;top:116px"><div class="n">01</div><b>Lorem ipsum dolor sit amet, consectetuer adipiscing elit, sed diam.</b>Lorem ipsum dolor sit amet, consectetuer adipiscing elit, sed diam nonummy nibh euismod tincidunt ut laoreet dolore magna aliquam erat volutpat. Ut wisi enim ad minim veniam, quis nostrud exerci tation ullamcorper suscipit lobortis nisl ut aliquip ex ea.</div>
  <div class="col" style="left:200px;top:116px"><div class="n">02</div><b>Lorem ipsum dolor sit amet, consectetuer adipiscing elit, sed diam.</b>Lorem ipsum dolor sit amet, consectetuer adipiscing elit, sed diam nonummy nibh euismod tincidunt ut laoreet dolore magna aliquam erat volutpat. Ut wisi enim ad minim veniam, quis nostrud exerci tation ullamcorper suscipit lobortis nisl ut aliquip ex ea.</div>
  <div class="col" style="left:360px;top:116px"><div class="n">03</div><b>Lorem ipsum dolor sit amet, consectetuer adipiscing elit, sed diam.</b>Lorem ipsum dolor sit amet, consectetuer adipiscing elit, sed diam nonummy nibh euismod tincidunt ut laoreet dolore magna aliquam erat volutpat. Ut wisi enim ad minim veniam, quis nostrud exerci tation ullamcorper suscipit lobortis nisl ut aliquip ex ea.</div>
  <div class="foot">Your presentation Title Goes Here | www.klarovenberg.de</div>
  <div class="pg">09</div>
</section>

<!-- Thank you -->
<section class="slide c1 r8">
  <div class="tile ph-grey" style="left:11px;top:-6px;width:108px;height:60px" role="img" aria-label="Foto: Behandlungsraum"></div>
  <div class="tile ph-green" style="left:11px;top:64px;width:108px;height:170px" role="img" aria-label="Foto: Tierarzt untersucht ein Pferd"></div>
  <div class="tile ph-grey" style="left:11px;top:244px;width:108px;height:60px" role="img" aria-label="Foto: Praxisflur"></div>
  <div class="tile ph-grey" style="left:128px;top:-6px;width:108px;height:70px" role="img" aria-label="Foto: Praxiseingang"></div>
  <div class="tile ph-portrait" style="left:128px;top:74px;width:108px;height:105px" role="img" aria-label="Foto: Team im Besprechungsraum"></div>
  <div class="tile ph-dog" style="left:128px;top:188px;width:108px;height:110px" role="img" aria-label="Foto: Golden Retriever"></div>
  <div class="logo" style="left:298px;top:46px"><i></i><b>KLAROVEN</b></div>
  <h2 class="hero" style="left:298px;top:118px">Thank You for<br><span class="y">Your Attention</span></h2>
  <div class="btn" style="left:298px;top:184px;width:183px"><svg><use href="#i-play"/></svg>Lorem ipsum dolor sit amet</div>
  <div class="meta" style="left:20px">info@klarovenberg.de | www.klarovenberg.de</div>
  <div class="meta" style="left:338px">07 Februar 2025 | Created by Max Mustermann</div>
</section>
</body>
</html>
```